Some graphics for our website

Okay here is what we need if you are up to it!

Check out our website www.budgetslatehub.com

We need a graphic to replace the main one on the home page with the tablets. Get creative. The only thing we are selling is the tablet you see pictured there. We are selling it in 6 colors Black White Orange Blue Red Green. The model if you want to look it up is k47. You can find many pictures on the net to edit and make our own that way. Anyways for the homepage spash image we would like 2 or 3 as they will rotate every 45 seconds. Get creative Think what will attract the customer to click buy yours now!

Then clicking to buy we need images made for each color that look uniform. so 6 images.

An image or two for the warranty and about us pages would complete it.

```html
<!DOCTYPE html>
<html lang="en">
<head>
<meta charset="utf-8">
<title>Tablet colour banners</title>
<link rel="stylesheet" href="https://fonts.googleapis.com/css2?family=Cabin+Sketch:wght@700&family=Cinzel:wght@400;600&display=swap">
<style>
  :root {
    --page: #ffffff;
    --ink-light: #ffffff;
    --ink-dark: #231f20;
    --bubble: #1a1718;
    --screen: #141414;
    --accent-teal: #1fb3c4;
    --accent-yellow: #f2b21c;
  }
  html, body {
    margin: 0;
    width: 1200px;
    height: 1112px;
    overflow: hidden;
    background: var(--page);
  }
  .sheet { position: relative; width: 1200px; height: 1112px; }
  .banner { position: absolute; display: block; }
  .banner svg { width: 100%; height: 100%; display: block; }

  .banner--blue   { left: 72px;  top: 35px;  width: 504px; height: 314px; --bg: #3d4fb4; --bg2: #c9283a; --tablet: #2a40c4; --ring: #3948b0; --ink: var(--ink-light); }
  .banner--black  { left: 641px; top: 31px;  width: 519px; height: 318px; --bg: #231f20; --bg2: #b4262f; --tablet: #3b3b3b; --ring: #231f20; --ink: var(--ink-light); }
  .banner--green  { left: 72px;  top: 377px; width: 511px; height: 317px; --bg: #1f9a3e; --bg2: #c9283a; --tablet: #43c443; --ring: #1f9a3e; --ink: var(--ink-light); }
  .banner--orange { left: 641px; top: 377px; width: 515px; height: 321px; --bg: #ec5a24; --bg2: #d42a2a; --tablet: #e0521f; --ring: #e8552a; --ink: var(--ink-light); }
  .banner--red    { left: 72px;  top: 735px; width: 517px; height: 321px; --bg: #e32228; --bg2: #f08a1c; --tablet: #d8232a; --ring: #e32228; --ink: var(--ink-light); }
  .banner--white  { left: 641px; top: 735px; width: 525px; height: 325px; --bg: #f4f1ef; --bg2: #ea6d63; --tablet: #dadada; --ring: transparent; --ink: var(--ink-dark); }

  .stop-main { stop-color: var(--bg); }
  .stop-warm { stop-color: var(--bg2); }
  .stop-teal { stop-color: var(--accent-teal); }
  .stop-yellow { stop-color: var(--accent-yellow); }

  .tablet-body { fill: var(--tablet); }
  .tablet-screen { fill: var(--screen); }
  .price-ring { fill: var(--ring); stroke: var(--ink); stroke-width: 3; }
  .banner--white .price-ring { stroke: none; }
  .price {
    font-family: "Cabin Sketch", cursive;
    font-weight: 700;
    font-size: 66px;
    fill: var(--ink);
  }
  .price-sign {
    font-family: "Cinzel", serif;
    font-weight: 600;
    font-size: 16px;
    fill: var(--ink);
  }
  .price-unit {
    font-family: "Cinzel", "Times New Roman", serif;
    font-size: 26px;
    fill: var(--ink);
  }
  .ship-bubble { fill: var(--bubble); }
  .ship-text {
    font-family: "Cinzel", "Times New Roman", serif;
    font-weight: 600;
    font-size: 15px;
    fill: var(--ink-light);
  }
</style>
</head>
<body>
<main class="sheet">

  <section class="banner banner--blue" aria-label="Blue tablet, 50 bucks, same day shipping">
    <svg viewBox="0 0 504 314" preserveAspectRatio="none">
      <defs>
        <radialGradient id="bg-blue" cx="35%" cy="65%" r="80%">
          <stop offset="0" class="stop-warm"/><stop offset="0.45" class="stop-teal"/><stop offset="0.75" class="stop-yellow"/><stop offset="1" class="stop-main"/>
        </radialGradient>
      </defs>
      <rect width="504" height="314" fill="url(#bg-blue)" role="img" aria-label="Overlapping coloured bubble pattern"/>
      <g role="img" aria-label="Photo of the blue tablet, back and front">
        <rect class="tablet-body" x="143" y="38" width="92" height="200" rx="8"/>
        <rect class="tablet-body" x="183" y="104" width="192" height="134" rx="10"/>
        <rect class="tablet-screen" x="205" y="116" width="148" height="104" rx="2"/>
      </g>
      <circle class="price-ring" cx="339" cy="66" r="58"/>
      <text class="price-sign" x="302" y="50">$</text>
      <text class="price" x="345" y="94" text-anchor="middle" textLength="72" lengthAdjust="spacingAndGlyphs">50</text>
      <text class="price-unit" x="401" y="77" textLength="88" lengthAdjust="spacingAndGlyphs">BUCKS</text>
      <g class="ship-bubble">
        <circle cx="88" cy="242" r="54"/>
        <path d="M125 280 Q148 272 160 246 Q158 285 112 293 Z"/>
      </g>
      <text class="ship-text" x="57" y="226" textLength="42" lengthAdjust="spacingAndGlyphs">SAME</text>
      <text class="ship-text" x="57" y="246" textLength="30" lengthAdjust="spacingAndGlyphs">DAY</text>
      <text class="ship-text" x="57" y="266" textLength="66" lengthAdjust="spacingAndGlyphs">SHIPPING</text>
    </svg>
  </section>

  <section class="banner banner--black" aria-label="Black tablet, 50 bucks, same day shipping">
    <svg viewBox="0 0 504 314" preserveAspectRatio="none">
      <defs>
        <radialGradient id="bg-black" cx="45%" cy="65%" r="80%">
          <stop offset="0" class="stop-warm"/><stop offset="0.4" class="stop-teal"/><stop offset="0.7" class="stop-warm"/><stop offset="1" class="stop-main"/>
        </radialGradient>
      </defs>
      <rect width="504" height="314" fill="url(#bg-black)" role="img" aria-label="Overlapping coloured bubble pattern"/>
      <g role="img" aria-label="Photo of the black tablet, back and front">
        <rect class="tablet-body" x="143" y="38" width="92" height="200" rx="8"/>
        <rect class="tablet-body" x="183" y="104" width="192" height="134" rx="10"/>
        <rect class="tablet-screen" x="205" y="116" width="148" height="104" rx="2"/>
      </g>
      <circle class="price-ring" cx="339" cy="66" r="58"/>
      <text class="price-sign" x="302" y="50">$</text>
      <text class="price" x="345" y="94" text-anchor="middle" textLength="72" lengthAdjust="spacingAndGlyphs">50</text>
      <text class="price-unit" x="401" y="77" textLength="88" lengthAdjust="spacingAndGlyphs">BUCKS</text>
      <g class="ship-bubble">
        <circle cx="88" cy="242" r="54"/>
        <path d="M125 280 Q148 272 160 246 Q158 285 112 293 Z"/>
      </g>
      <text class="ship-text" x="57" y="226" textLength="42" lengthAdjust="spacingAndGlyphs">SAME</text>
      <text class="ship-text" x="57" y="246" textLength="30" lengthAdjust="spacingAndGlyphs">DAY</text>
      <text class="ship-text" x="57" y="266" textLength="66" lengthAdjust="spacingAndGlyphs">SHIPPING</text>
    </svg>
  </section>

  <section class="banner banner--green" aria-label="Green tablet, 50 bucks, same day shipping">
    <svg viewBox="0 0 504 314" preserveAspectRatio="none">
      <defs>
        <radialGradient id="bg-green" cx="40%" cy="65%" r="80%">
          <stop offset="0" class="stop-warm"/><stop offset="0.45" class="stop-teal"/><stop offset="0.75" class="stop-yellow"/><stop offset="1" class="stop-main"/>
        </radialGradient>
      </defs>
      <rect width="504" height="314" fill="url(#bg-green)" role="img" aria-label="Overlapping coloured bubble pattern"/>
      <g role="img" aria-label="Photo of the green tablet, back and front">
        <rect class="tablet-body" x="143" y="38" width="92" height="200" rx="8"/>
        <rect class="tablet-body" x="183" y="104" width="192" height="134" rx="10"/>
        <rect class="tablet-screen" x="205" y="116" width="148" height="104" rx="2"/>
      </g>
      <circle class="price-ring" cx="339" cy="66" r="58"/>
      <text class="price-sign" x="302" y="50">$</text>
      <text class="price" x="345" y="94" text-anchor="middle" textLength="72" lengthAdjust="spacingAndGlyphs">50</text>
      <text class="price-unit" x="401" y="77" textLength="88" lengthAdjust="spacingAndGlyphs">BUCKS</text>
      <g class="ship-bubble">
        <circle cx="88" cy="242" r="54"/>
        <path d="M125 280 Q148 272 160 246 Q158 285 112 293 Z"/>
      </g>
      <text class="ship-text" x="57" y="226" textLength="42" lengthAdjust="spacingAndGlyphs">SAME</text>
      <text class="ship-text" x="57" y="246" textLength="30" lengthAdjust="spacingAndGlyphs">DAY</text>
      <text class="ship-text" x="57" y="266" textLength="66" lengthAdjust="spacingAndGlyphs">SHIPPING</text>
    </svg>
  </section>

  <section class="banner banner--orange" aria-label="Orange tablet, 50 bucks, same day shipping">
    <svg viewBox="0 0 504 314" preserveAspectRatio="none">
      <defs>
        <radialGradient id="bg-orange" cx="40%" cy="65%" r="80%">
          <stop offset="0" class="stop-warm"/><stop offset="0.45" class="stop-yellow"/><stop offset="0.7" class="stop-teal"/><stop offset="1" class="stop-main"/>
        </radialGradient>
      </defs>
      <rect width="504" height="314" fill="url(#bg-orange)" role="img" aria-label="Overlapping coloured bubble pattern"/>
      <g role="img" aria-label="Photo of the orange tablet, back and front">
        <rect class="tablet-body" x="143" y="38" width="92" height="200" rx="8"/>
        <rect class="tablet-body" x="183" y="104" width="192" height="134" rx="10"/>
        <rect class="tablet-screen" x="205" y="116" width="148" height="104" rx="2"/>
      </g>
      <circle class="price-ring" cx="339" cy="66" r="58"/>
      <text class="price-sign" x="302" y="50">$</text>
      <text class="price" x="345" y="94" text-anchor="middle" textLength="72" lengthAdjust="spacingAndGlyphs">50</text>
      <text class="price-unit" x="401" y="77" textLength="88" lengthAdjust="spacingAndGlyphs">BUCKS</text>
      <g class="ship-bubble">
        <circle cx="88" cy="242" r="54"/>
        <path d="M125 280 Q148 272 160 246 Q158 285 112 293 Z"/>
      </g>
      <text class="ship-text" x="57" y="226" textLength="42" lengthAdjust="spacingAndGlyphs">SAME</text>
      <text class="ship-text" x="57" y="246" textLength="30" lengthAdjust="spacingAndGlyphs">DAY</text>
      <text class="ship-text" x="57" y="266" textLength="66" lengthAdjust="spacingAndGlyphs">SHIPPING</text>
    </svg>
  </section>

  <section class="banner banner--red" aria-label="Red tablet, 50 bucks, same day shipping">
    <svg viewBox="0 0 504 314" preserveAspectRatio="none">
      <defs>
        <radialGradient id="bg-red" cx="40%" cy="65%" r="80%">
          <stop offset="0" class="stop-warm"/><stop offset="0.45" class="stop-teal"/><stop offset="0.7" class="stop-yellow"/><stop offset="1" class="stop-main"/>
        </radialGradient>
      </defs>
      <rect width="504" height="314" fill="url(#bg-red)" role="img" aria-label="Overlapping coloured bubble pattern"/>
      <g role="img" aria-label="Photo of the red tablet, back and front">
        <rect class="tablet-body" x="143" y="38" width="92" height="200" rx="8"/>
        <rect class="tablet-body" x="183" y="104" width="192" height="134" rx="10"/>
        <rect class="tablet-screen" x="205" y="116" width="148" height="104" rx="2"/>
      </g>
      <circle class="price-ring" cx="339" cy="66" r="58"/>
      <text class="price-sign" x="302" y="50">$</text>
      <text class="price" x="345" y="94" text-anchor="middle" textLength="72" lengthAdjust="spacingAndGlyphs">50</text>
      <text class="price-unit" x="401" y="77" textLength="88" lengthAdjust="spacingAndGlyphs">BUCKS</text>
      <g class="ship-bubble">
        <circle cx="88" cy="242" r="54"/>
        <path d="M125 280 Q148 272 160 246 Q158 285 112 293 Z"/>
      </g>
      <text class="ship-text" x="57" y="226" textLength="42" lengthAdjust="spacingAndGlyphs">SAME</text>
      <text class="ship-text" x="57" y="246" textLength="30" lengthAdjust="spacingAndGlyphs">DAY</text>
      <text class="ship-text" x="57" y="266" textLength="66" lengthAdjust="spacingAndGlyphs">SHIPPING</text>
    </svg>
  </section>

  <section class="banner banner--white" aria-label="White tablet, 50 bucks, same day shipping">
    <svg viewBox="0 0 504 314" preserveAspectRatio="none">
      <defs>
        <radialGradient id="bg-white" cx="40%" cy="65%" r="80%">
          <stop offset="0" class="stop-main"/><stop offset="0.4" class="stop-warm"/><stop offset="0.7" class="stop-teal"/><stop offset="1" class="stop-main"/>
        </radialGradient>
      </defs>
      <rect width="504" height="314" fill="url(#bg-white)" role="img" aria-label="Overlapping soft coloured bubble pattern"/>
      <g role="img" aria-label="Photo of the white tablet, back and front">
        <rect class="tablet-body" x="143" y="38" width="92" height="200" rx="8"/>
        <rect class="tablet-body" x="183" y="104" width="192" height="134" rx="10"/>
        <rect class="tablet-screen" x="205" y="116" width="148" height="104" rx="2"/>
      </g>
      <circle class="price-ring" cx="339" cy="66" r="58"/>
      <text class="price-sign" x="302" y="50">$</text>
      <text class="price" x="345" y="94" text-anchor="middle" textLength="72" lengthAdjust="spacingAndGlyphs">50</text>
      <text class="price-unit" x="401" y="77" textLength="88" lengthAdjust="spacingAndGlyphs">BUCKS</text>
      <g class="ship-bubble">
        <circle cx="88" cy="242" r="54"/>
        <path d="M125 280 Q148 272 160 246 Q158 285 112 293 Z"/>
      </g>
      <text class="ship-text" x="57" y="226" textLength="42" lengthAdjust="spacingAndGlyphs">SAME</text>
      <text class="ship-text" x="57" y="246" textLength="30" lengthAdjust="spacingAndGlyphs">DAY</text>
      <text class="ship-text" x="57" y="266" textLength="66" lengthAdjust="spacingAndGlyphs">SHIPPING</text>
    </svg>
  </section>

</main>
</body>
</html>
```